Rare Glow Edibles Gummies

Packaging design for custom mylars for cannabis infused gummies. I need a space for a warning label, nutrition facts, ingredients, brand logo and then individualized item details. We will later be doing assorted peanut butter cups, hard candies, etc.

```html
<!DOCTYPE html>
<html lang="en">
<head>
<meta charset="utf-8">
<title>Rare Glow Edibles – Cannabis Infused Gummies Pouch Front</title>
<link href="https://fonts.googleapis.com/css2?family=Bebas+Neue&family=Indie+Flower&display=swap" rel="stylesheet">
<style>
  :root {
    --backdrop: #b3b3b3;
    --pouch-black: #12110e;
    --teal: #0fa39b;
    --white: #ffffff;
    --rule-grey: #8a8a8a;
    --leaf-dark: #1c3a1c;
    --leaf-mid: #3f7a34;
    --leaf-light: #5f9a4a;
  }
  * { box-sizing: border-box; margin: 0; padding: 0; }
  html, body {
    width: 720px;
    height: 1200px;
    overflow: hidden;
    background: var(--backdrop);
  }
  .pouch-front {
    position: absolute;
    left: 20px;
    top: 124px;
    width: 680px;
    height: 952px;
    background: var(--pouch-black);
    overflow: hidden;
  }
  .leaf-border {
    position: absolute;
    left: 0;
    bottom: 0;
    width: 680px;
    height: 300px;
  }
  .brand-ring {
    position: absolute;
    left: 200px;
    top: 191px;
    width: 194px;
    height: 194px;
    border: 2px solid var(--rule-grey);
    border-radius: 50%;
    display: flex;
    align-items: center;
    justify-content: center;
  }
  .brand-name {
    text-align: center;
    font-family: "Bebas Neue", sans-serif;
    font-size: 38px;
    line-height: 0.95;
    letter-spacing: 1px;
    color: var(--teal);
  }
  .brand-name span { display: block; }
  .product-type {
    position: absolute;
    left: 0;
    width: 680px;
    top: 404px;
    text-align: center;
    font-family: "Bebas Neue", sans-serif;
    font-weight: 400;
    font-size: 128px;
    line-height: 1;
    letter-spacing: 1px;
    color: var(--teal);
  }
  .product-subtitle {
    position: absolute;
    left: 0;
    width: 680px;
    top: 514px;
    text-align: center;
    font-family: "Indie Flower", cursive;
    font-size: 52px;
    line-height: 1;
    color: var(--white);
  }
  .divider {
    position: absolute;
    left: 289px;
    top: 605px;
    width: 102px;
    height: 2px;
    background: var(--white);
    opacity: 0.85;
  }
  .feature-icons {
    position: absolute;
    left: 0;
    top: 636px;
    width: 680px;
    height: 92px;
  }
  .net-contents {
    position: absolute;
    left: 0;
    width: 680px;
    top: 760px;
    text-align: center;
    font-family: "Bebas Neue", sans-serif;
    font-size: 26px;
    line-height: 1;
    color: var(--white);
    word-spacing: 2px;
  }
  .net-contents .sep { margin: 0 10px; }
</style>
</head>
<body>
  <main class="pouch-front">
    <svg class="leaf-border" viewBox="0 0 680 300" role="img" aria-label="Illustrated cannabis leaves framing the bottom of the pouch">
      <defs>
        <linearGradient id="leafTone" x1="0" y1="0" x2="0" y2="1">
          <stop offset="0" stop-color="#5f9a4a"/>
          <stop offset="0.5" stop-color="#3f7a34"/>
          <stop offset="1" stop-color="#1c3a1c"/>
        </linearGradient>
      </defs>
      <path fill="url(#leafTone)" d="M0 20 C40 40 70 90 110 120 C150 150 170 170 200 160 C230 150 240 170 260 175 C300 180 320 170 340 172 C360 170 380 180 420 175 C440 170 450 150 480 160 C510 170 530 150 570 120 C610 90 640 40 680 10 L680 300 L0 300 Z"/>
    </svg>

    <div class="brand-ring">
      <div class="brand-name"><span>Rare Glow</span><span>Edibles</span></div>
    </div>

    <h1 class="product-type">CANNABIS</h1>
    <p class="product-subtitle">Infused Gummies</p>
    <div class="divider"></div>

    <svg class="feature-icons" viewBox="0 0 680 92" aria-label="Product icons: cannabis, warning, formula">
      <g fill="none" stroke="#0fa39b" stroke-width="2.5">
        <circle cx="216" cy="46" r="44"/>
        <circle cx="340" cy="46" r="44"/>
        <circle cx="464" cy="46" r="44"/>
      </g>
      <g class="icon-leaf" fill="#0fa39b">
        <path d="M216 22 L222 42 L216 52 L210 42 Z"/>
        <path d="M196 34 L214 46 L215 52 L204 46 Z"/>
        <path d="M236 34 L218 46 L217 52 L228 46 Z"/>
        <path d="M196 56 L214 52 L216 55 Z"/>
        <path d="M236 56 L218 52 L216 55 Z"/>
        <rect x="215" y="52" width="2" height="14"/>
      </g>
      <g class="icon-warning">
        <path d="M340 26 L361 62 L319 62 Z" fill="#0fa39b"/>
        <rect x="338" y="38" width="4" height="13" fill="#12110e"/>
        <circle cx="340" cy="56" r="2.3" fill="#12110e"/>
      </g>
      <g class="icon-molecule" fill="none" stroke="#0fa39b" stroke-width="2.5">
        <polygon points="458,37 466,41.5 466,50.5 458,55 450,50.5 450,41.5"/>
        <polygon points="474,37 482,41.5 482,50.5 474,55 466,50.5 466,41.5"/>
        <polygon points="466,51 474,55.5 474,64.5 466,69 458,64.5 458,55.5"/>
        <circle cx="452" cy="30" r="2" fill="#0fa39b"/>
        <circle cx="486" cy="60" r="2" fill="#0fa39b"/>
      </g>
    </svg>

    <p class="net-contents">20 GUMMIES<span class="sep">|</span>100G (3.4OZ) NE WT.</p>
  </main>
</body>
</html>
```